Voice Over IP Service

Create a 1-2 page brochure for our voice over IP phone system service.

The color pallet should use these colors..
#e23232 red
#636466 Grey
#434445 Dark grey

```html
<!DOCTYPE html>
<html lang="en">
<head>
<meta charset="utf-8">
<title>Norvell Connect – Hosted VoIP Brochure</title>
<link rel="stylesheet" href="https://fonts.googleapis.com/css2?family=Nunito+Sans:wght@400;600;700;800&family=Oswald:wght@400;500&family=Roboto:wght@500;700&display=swap">
<style>
  :root{
    --red:#e23232;
    --red-deep:#c82424;
    --grey:#636466;
    --grey-dark:#434445;
    --line:#d9dadc;
    --white:#ffffff;
    --canvas:#e4e5e7;
  }
  *{margin:0;padding:0;box-sizing:border-box}
  html,body{width:1200px;height:841px;overflow:hidden}
  body{background:var(--canvas);font-family:"Nunito Sans",Arial,sans-serif;color:var(--grey);position:relative}
  .page{position:absolute;top:58px;width:560px;height:725px;background:var(--white);overflow:hidden;box-shadow:0 2px 10px rgba(0,0,0,.18)}
  .page--front{left:30px}
  .page--back{left:610px}

  .brand{position:absolute;left:20px;top:32px;display:flex;align-items:center;gap:8px}
  .brand__mark{width:26px;height:26px;border:3px solid var(--red);border-radius:4px}
  .brand__name{font-weight:800;font-size:25px;color:var(--red);letter-spacing:-.5px;line-height:1}
  .tagline{position:absolute;right:14px;top:22px;text-align:right;font-family:"Oswald",sans-serif;font-weight:400;font-size:15px;line-height:19px;color:var(--grey-dark);text-transform:uppercase}

  .hero{position:absolute;left:0;top:92px;width:560px;height:217px}
  .hero__photo{position:absolute;left:190px;top:0;right:0;bottom:0;background:linear-gradient(135deg,#d8d9dc 0%,#b79a7c 45%,#8c735c 70%,#e9eaec 100%)}
  .hero__panel{position:absolute;left:0;top:0;width:340px;height:217px;background:var(--red-deep);clip-path:polygon(0 0,246px 0,340px 100%,0 100%)}
  .hero__title{position:absolute;left:20px;top:40px;color:var(--white);font-weight:700;font-size:17px;line-height:26px;text-transform:uppercase}
  .hero__rule{position:absolute;left:20px;top:98px;width:110px;height:2px;background:var(--white)}
  .hero__lead{position:absolute;left:20px;top:125px;color:var(--white);font-weight:800;font-size:9.5px}
  .hero__text{position:absolute;left:20px;top:140px;width:272px;color:var(--white);font-size:8.6px;line-height:13px;text-align:justify}

  .col{position:absolute;top:340px;width:252px}
  .col--left{left:20px}
  .col--right{left:290px}
  .col h3{font-size:10px;font-weight:800;color:var(--grey-dark);text-transform:uppercase;margin-bottom:8px}
  .col p{font-size:8.8px;line-height:11.5px;text-align:justify}

  .banner{position:absolute;left:0;top:416px;width:380px;height:24px;background:var(--red);clip-path:polygon(0 0,366px 0,380px 100%,0 100%);color:var(--white);font-weight:700;font-size:12.5px;line-height:24px;padding-left:20px;text-transform:uppercase}
  .intro{position:absolute;left:20px;top:452px;width:520px;font-size:8.8px;line-height:11.5px}
  .vendor{position:absolute;left:20px;top:485px;color:var(--red);font-weight:800;font-size:12px;line-height:17px}

  .services{position:absolute;left:20px;top:530px;list-style:none}
  .services li{display:flex;align-items:center;height:31px;font-family:"Roboto",sans-serif;font-weight:700;font-size:10.5px;letter-spacing:1.2px;color:var(--grey)}
  .services svg{width:25px;height:25px;margin-right:12px}

  .devices{position:absolute;left:219px;top:516px;width:334px;height:151px;background:linear-gradient(160deg,#2b2c2e 0%,#6f7275 50%,#e7e8ea 100%);border-radius:4px}

  .footer{position:absolute;left:0;bottom:0;width:560px;height:34px;background:var(--grey)}
  .footer__cta{position:absolute;left:25px;top:5px;color:var(--white);font-size:9.5px;line-height:12px}
  .footer__cta b{font-weight:800}
  .footer__web{position:absolute;right:0;top:0;width:213px;height:34px;background:var(--red);clip-path:polygon(22px 0,100% 0,100% 100%,0 100%);display:flex;align-items:center;justify-content:flex-end;padding-right:20px;gap:6px;color:var(--white);font-family:"Roboto",sans-serif;font-weight:700;font-size:11px;letter-spacing:1px}
  .footer__web i{width:8px;height:8px;border-radius:50%;background:var(--white);display:block}

  .benefits{position:absolute;left:0;top:92px;width:560px;height:217px;background:linear-gradient(90deg,#ffffff 0%,#eef1f4 55%,#dfe4ea 100%)}
  .person{position:absolute;left:435px;top:187px;width:125px;height:188px;background:linear-gradient(180deg,#e9c9a6 0%,#b6b9bd 35%,#8d9094 100%);border-radius:50px 50px 0 0}

  .band{position:absolute;left:0;top:309px;width:560px;height:66px;background:var(--red-deep);color:var(--white);font-weight:700;font-size:14.5px;line-height:66px;padding-left:20px;text-transform:uppercase}

  .feature{position:absolute;width:255px;display:flex;gap:10px}
  .feature__icon{flex:none;width:53px;height:53px;border:2px solid var(--red);border-radius:4px;background:linear-gradient(135deg,#fff,#eef0f2);display:flex;align-items:center;justify-content:center}
  .feature__icon svg{width:30px;height:30px}
  .feature h4{color:var(--red);font-weight:800;font-size:11px;margin:2px 0 3px}
  .feature p{font-size:7.4px;line-height:9px;text-align:justify;color:var(--grey-dark)}
  .feature--l{left:18px}
  .feature--r{left:291px}
  .divider{position:absolute;left:18px;width:524px;border-top:1px dashed var(--line)}
  .deskphone{position:absolute;left:398px;top:578px;width:147px;height:96px;background:linear-gradient(150deg,#3a3b3d 0%,#1f2021 60%,#6a6c6f 100%);border-radius:6px}
</style>
</head>
<body>

<section class="page page--front">
  <div class="brand"><span class="brand__mark"></span><span class="brand__name">NorvellConnect</span></div>
  <div class="tagline">Americas most popular phone system<br>Voice over IP (VoIP)</div>

  <div class="hero">
    <div class="hero__photo" role="img" aria-label="Photo of a team meeting around a table with a video conference screen and a desk phone"></div>
    <div class="hero__panel"></div>
    <h1 class="hero__title">Is it time for a<br>better phone system?</h1>
    <div class="hero__rule"></div>
    <p class="hero__lead">Why Choose Our Hosted VOIP Phone Service?</p>
    <p class="hero__text">At Norvell Connect our business phone service is best-of-breed that utilizes redundant servers in geographically disperse regions throughout the country to ensure high reliability and sound quality.</p>
  </div>

  <div class="col col--left">
    <h3>What is VoIP?</h3>
    <p>VOIP offers a very versatile, low-cost solution for phones and communication that can easily scale with the growth of your business.</p>
  </div>
  <div class="col col--right">
    <h3>Hosted VoIP phone system</h3>
    <p>A fully featured phone system that runs in the cloud with an easy-access online portal for administration and user management. VOIP includes routing work-flows, music on hold, call queues, web phone app and much more.</p>
  </div>

  <div class="banner">Why choose our hosted VoIP phone service?</div>
  <p class="intro">At Norvell Connect our business phone service is best-of-breed that utilizes redundant servers in geographically disperse regions throughout the country to ensure high reliability and sound quality.</p>
  <p class="vendor">We are a full-service VOIP phone system vendor.<br>Our services include...</p>

  <ul class="services">
    <li><svg viewBox="0 0 25 25"><rect x="1" y="1" width="23" height="23" rx="3" fill="none" stroke="#636466" stroke-width="1.5"/><circle cx="12.5" cy="12.5" r="6" fill="none" stroke="#434445" stroke-width="1.6"/><path d="M12.5 9v4l3 2" stroke="#434445" stroke-width="1.6" fill="none"/></svg>PLANNING</li>
    <li><svg viewBox="0 0 25 25"><rect x="1" y="1" width="23" height="23" rx="3" fill="none" stroke="#636466" stroke-width="1.5"/><rect x="5" y="6" width="4" height="13" rx="1" fill="#434445"/><rect x="10" y="8" width="10" height="11" rx="1" fill="none" stroke="#434445" stroke-width="1.4"/><path d="M12 11h6M12 14h6M12 17h6" stroke="#434445" stroke-width="1"/></svg>PHONE SALES</li>
    <li><svg viewBox="0 0 25 25"><rect x="1" y="1" width="23" height="23" rx="3" fill="none" stroke="#636466" stroke-width="1.5"/><circle cx="10" cy="14" r="4.5" fill="none" stroke="#434445" stroke-width="2.4" stroke-dasharray="2.2 1.3"/><circle cx="16.5" cy="8" r="3" fill="none" stroke="#434445" stroke-width="1.8" stroke-dasharray="1.6 1"/></svg>INSTALLATION</li>
    <li><svg viewBox="0 0 25 25"><rect x="1" y="1" width="23" height="23" rx="3" fill="none" stroke="#636466" stroke-width="1.5"/><circle cx="12.5" cy="9" r="3.6" fill="#434445"/><path d="M5 21c0-5 3.5-7 7.5-7s7.5 2 7.5 7z" fill="#434445"/></svg>SUPPORT</li>
    <li><svg viewBox="0 0 25 25"><rect x="1" y="1" width="23" height="23" rx="3" fill="none" stroke="#636466" stroke-width="1.5"/><circle cx="12.5" cy="9" r="3" fill="#434445"/><circle cx="6.5" cy="11" r="2.2" fill="#434445"/><circle cx="18.5" cy="11" r="2.2" fill="#434445"/><path d="M7 20c0-4 2.5-6 5.5-6s5.5 2 5.5 6z M2.5 19c0-3 1.8-4.5 4-4.5 M22.5 19c0-3-1.8-4.5-4-4.5" fill="#434445" stroke="#434445" stroke-width="1"/></svg>MANAGEMENT</li>
  </ul>

  <div class="devices" role="img" aria-label="Illustration of desktop monitor, laptop, tablet and phone showing video calls and a dashboard"></div>

  <footer class="footer">
    <p class="footer__cta">Call us direct at &#9990; <b>555-014-2290</b> to get a FREE consultation<br>or demonstration with absolutely no pressure or obligation</p>
    <div class="footer__web"><i></i>www.norvellconnect.com</div>
  </footer>
</section>

<section class="page page--back">
  <div class="brand"><span class="brand__mark"></span><span class="brand__name">NorvellConnect</span></div>
  <div class="tagline">Americas most popular phone system<br>Voice over IP (VoIP)</div>

  <div class="benefits" role="img" aria-label="Infographic of the benefits of VoIP telephony: mobility, call routing and automation, even playing field for small businesses, less maintenance and no geographic restrictions"></div>

  <div class="band">Additionally, people appreciate the following...</div>
  <div class="person" role="img" aria-label="Photo of a smiling businessman in a grey suit with arms crossed"></div>

  <div class="feature feature--l" style="top:397px">
    <div class="feature__icon"><svg viewBox="0 0 30 30"><rect x="8" y="3" width="14" height="24" rx="2" fill="none" stroke="#434445" stroke-width="1.8"/><text x="15" y="19" text-anchor="middle" font-family="Nunito Sans, sans-serif" font-weight="800" font-size="11" fill="#e23232">$</text></svg></div>
    <div><h4>Competitive pricing:</h4><p>Low flat-fee pricing for unlimited local and long-distance phone service. Our pricing includes an extensive feature list that includes routing by time-frames, easy to create work-flows, company greeting and menu-list (Auto Attendant), ring-all or find the available staff member, call-center reporting and more.</p></div>
  </div>
  <div class="feature feature--r" style="top:397px">
    <div class="feature__icon"><svg viewBox="0 0 30 30"><rect x="4" y="6" width="6" height="19" rx="1.5" fill="#434445"/><rect x="11" y="8" width="15" height="17" rx="1.5" fill="none" stroke="#434445" stroke-width="1.8"/><path d="M14 13h9M14 17h9M14 21h9" stroke="#434445" stroke-width="1.4" stroke-dasharray="2 1.5"/></svg></div>
    <div><h4>Quality phones</h4><p>We include business phones by Veltrix and we support most VOIP phone manufacturers including Orano, Pellcom, Kestro and many others.</p></div>
  </div>

  <div class="divider" style="top:488px"></div>

  <div class="feature feature--l" style="top:500px">
    <div class="feature__icon"><svg viewBox="0 0 30 30"><rect x="7" y="3" width="16" height="20" rx="1.5" fill="none" stroke="#434445" stroke-width="1.8"/><circle cx="13" cy="17" r="6" fill="none" stroke="#434445" stroke-width="2"/><path d="M9 21l-5 6" stroke="#434445" stroke-width="2.5"/><path d="M17 8v8M20 11v5" stroke="#e23232" stroke-width="2"/></svg></div>
    <div><h4>No set-up fees!</h4><p>Let us do the heavy-lifting. We will plan and configure your dream phone system as part of our service.</p></div>
  </div>
  <div class="feature feature--r" style="top:500px">
    <div class="feature__icon"><svg viewBox="0 0 30 30"><rect x="6" y="3" width="18" height="11" rx="2" fill="none" stroke="#434445" stroke-width="1.6"/><path d="M9 7h12M9 10h9" stroke="#434445" stroke-width="1.2"/><circle cx="15" cy="19" r="3.5" fill="#434445"/><path d="M8 28c0-4 3-5.5 7-5.5s7 1.5 7 5.5z" fill="#434445"/></svg></div>
    <div><h4>Call Center</h4><p>Track stats on call-center flow, abandoned calls, voicemails, hold times, and more. Our granular reports and call center manager portal allow you to manage your team better than ever.</p></div>
  </div>

  <div class="divider" style="top:568px"></div>

  <div class="feature feature--l" style="top:582px">
    <div class="feature__icon"><svg viewBox="0 0 30 30"><rect x="3" y="5" width="24" height="16" rx="1.5" fill="none" stroke="#434445" stroke-width="1.8"/><path d="M12 9.5v7l6-3.5z" fill="#e23232"/><path d="M11 25h8M15 21v4" stroke="#434445" stroke-width="1.8"/></svg></div>
    <div><h4>Audio &amp; Video Conferencing</h4><p>Audio conferencing and video conferencing are a rising need for modern business. Remove the need for multiple applications and handle all client communication under one platform.</p></div>
  </div>

  <div class="deskphone" role="img" aria-label="Photo of a black business desk phone with a colour touch screen"></div>

  <footer class="footer">
    <p class="footer__cta">Call us direct at &#9990; <b>555-014-2290</b> to get a FREE consultation<br>or demonstration with absolutely no pressure or obligation</p>
    <div class="footer__web"><i></i>www.norvellconnect.com</div>
  </footer>
</section>

</body>
</html>
```